Harlow's Crab Shack

Harlow’s Crab Shack

This project is a design of a restaurant referral card used for tourist and business travelers. It needs to be 2 sided, 4/1 front color, grayscale back. I am including the specs ie, the size of the card as well as a sample card. I am also including the some pics and text. I would like a few looks for this card.

I need a card with front and back with the following specs:

• Card size 4 inch height x 2 1/8 inch width
• Top: ¾ inch Logo/header on front of card
• Front: four color
• Back: Grayscale/ black and white
* FULL Bleed for print
***Note the logo needs to be at the top 3/4 inch on the front of the card***
Front of Card:
~Logo/Restaurant name “Harlow’s Crab Shack” (top ¾ inch of card front)
~Harlow’s seafood is flown in daily from New England. It is our goal to serve the freshest seafood available in the Traditional New England style.

~Family Owned and operated
~ Take Out Available
~386-517-2293
~Open 7 days a week 11AM-8:00PM
~2738 N Larkspur Rd New Smyrna Beach FL

www.harlowscrabshackqtz.com
~KIDS MENU $5.99

Back of Card:
~Logo/Restaurant name “Harlow’s Crab Shack”
~ Freshest seafood available in the Traditional New England style
~Specialties include: Haddock, Cod, Mahi, Flounder, Fried Oysters, Whole Belly Clams, NE Steamers, Crab Legs, Lobster Salad, & much more!!
~Map (included)
~386-517-2293
~Located on A1A

Please note you can add your own flare and verbage just need the highlighted points/text above to be the focus. Would like to highlight the Fresh Seafood aspect of this restaurant. BE CREATIVE
PS I attached a sample card of front and back for specs from another card.
Also would like to see sample of card with green background similar to green in logo
Thanks,
Gerald

Industry/Entity Type

Restaurant

Colors
9bcb3c

```html
<!DOCTYPE html>
<html lang="en">
<head>
<meta charset="utf-8">
<title>Harlow's Crab Shack – Referral Card</title>
<link rel="stylesheet" href="https://fonts.googleapis.com/css2?family=Anton&family=Arimo:ital,wght@0,400;0,700;1,700&family=Archivo+Black&family=Caveat:wght@600&family=IM+Fell+English&display=swap">
<style>
  :root {
    --blue-deep: #1655a8;
    --blue-mid: #2a7fd0;
    --blue-sky: #8fcdf2;
    --blue-pale: #d8eefb;
    --charcoal: #1d1d1d;
    --graphite: #4a4a4a;
    --silver: #eef0f3;
    --seal-silver: #d3d6da;
    --card-gray: #e6e6e6;
    --ink: #111;
    --white: #fff;
    --accent-red: #d81f1f;
  }
  * { box-sizing: border-box; margin: 0; padding: 0; }
  html, body { width: 1200px; height: 1109px; overflow: hidden; background: var(--white); }
  .canvas { position: relative; width: 1200px; height: 1109px; }

  .side { position: absolute; top: 23px; width: 551px; height: 1035px; }
  .side--front { left: 45px; }
  .side--back { left: 604px; }

  .masthead {
    position: absolute; left: 0; top: 0; width: 100%; height: 190px;
    display: flex; flex-direction: column; align-items: center; justify-content: center;
    font-family: "Anton", sans-serif; color: var(--silver); line-height: 1;
  }
  .side--front .masthead { background: linear-gradient(180deg, var(--blue-deep), var(--blue-mid) 55%, var(--blue-deep)); }
  .side--back .masthead { background: linear-gradient(180deg, var(--charcoal), var(--graphite) 55%, var(--charcoal)); }
  .masthead__top { font-size: 52px; letter-spacing: 2px; }
  .masthead__main { font-size: 86px; letter-spacing: 3px; margin-top: 4px; }

  .rule { position: absolute; left: 0; top: 205px; width: 100%; height: 6px;
    background: linear-gradient(90deg, #555, #ddd 50%, #555); }

  /* Front body */
  .front-body {
    position: absolute; left: 0; top: 210px; width: 100%; height: 825px; overflow: hidden;
    background: linear-gradient(180deg, var(--blue-pale) 0%, var(--blue-sky) 40%, var(--blue-mid) 100%);
  }
  .bubble { position: absolute; left: 308px; top: 20px; width: 262px; height: 262px; border-radius: 50%;
    background: radial-gradient(circle at 40% 35%, rgba(255,255,255,.85), rgba(190,225,248,.6) 70%, rgba(140,200,240,.4)); }
  .seal { position: absolute; left: 26px; top: 18px; width: 210px; height: 210px; border-radius: 50%;
    background: var(--seal-silver); }
  .seal-text { position: absolute; left: 26px; top: 18px; width: 210px; height: 210px;
    display: flex; flex-direction: column; align-items: center; justify-content: center;
    font-family: "Arimo", sans-serif; font-weight: 700; font-style: italic; color: var(--accent-red);
    font-size: 23px; line-height: 1.25; text-align: center; }

  .hours { position: absolute; left: 312px; top: 76px; font-family: "Arimo", sans-serif; }
  .hours__open { font-family: "Archivo Black", sans-serif; font-size: 46px; color: var(--white);
    -webkit-text-stroke: 1px #666; line-height: 1; letter-spacing: 1px; }
  .hours__days { font-family: "Archivo Black", sans-serif; font-size: 15px; color: var(--white);
    -webkit-text-stroke: .5px #555; margin-top: 2px; }
  .hours__range { font-family: "Anton", sans-serif; font-size: 22px; color: var(--ink); margin-top: 10px; letter-spacing: .5px; }
  .hours__time { font-size: 15px; color: var(--ink); margin-top: 6px; padding-left: 48px; }

  .takeaway { position: absolute; left: 198px; top: 240px; font-family: "Anton", sans-serif;
    font-size: 33px; color: var(--white); -webkit-text-stroke: 1px var(--blue-deep); letter-spacing: 1px; }
  .kids-menu { position: absolute; left: 262px; top: 286px; font-family: "Anton", sans-serif;
    font-size: 20px; color: var(--accent-red); letter-spacing: 1px; }

  .story { position: absolute; left: 0; top: 327px; width: 100%; text-align: center;
    font-family: "IM Fell English", serif; font-size: 23px; line-height: 39px; color: var(--ink); }

  .dish-photo { position: absolute; left: 0; top: 444px; width: 421px; height: 262px;
    border-radius: 0 50% 50% 0 / 0 50% 50% 0;
    background: radial-gradient(ellipse at 45% 50%, #f2a55a 0%, #e8d7b8 40%, #f6f6f4 70%, #c9dfee 100%); }

  .front-phone { position: absolute; left: 0; top: 712px; width: 100%; text-align: center;
    font-family: "Archivo Black", sans-serif; font-size: 58px; color: var(--white); letter-spacing: 4px; line-height: 1; }
  .front-address { position: absolute; left: 0; top: 774px; width: 100%; text-align: center;
    font-family: "Arimo", sans-serif; font-weight: 700; font-size: 23px; color: var(--ink); }
  .front-web { position: absolute; left: 0; top: 802px; width: 100%; text-align: center;
    font-family: "Arimo", sans-serif; font-size: 16px; color: var(--white); }

  /* Back body */
  .back-body { position: absolute; left: 0; top: 210px; width: 100%; height: 825px;
    background: linear-gradient(180deg, #f1f1f1 0px, #fafafa 200px, var(--white) 260px); }
  .tagline { position: absolute; left: 0; top: 20px; width: 100%; text-align: center;
    font-family: "Caveat", cursive; font-size: 38px; line-height: 47px; color: var(--ink); }

  .specialties { position: absolute; left: 35px; top: 165px; width: 479px; height: 396px; background: var(--charcoal); }
  .specialties__title { position: absolute; left: 0; top: 8px; width: 100%; text-align: center;
    font-family: "Arimo", sans-serif; font-weight: 700; font-style: italic; font-size: 48px; color: var(--white); letter-spacing: -1px; }
  .specialties__list { position: absolute; left: 11px; top: 79px; width: 457px; height: 271px; background: var(--card-gray);
    list-style: none; text-align: center; padding-top: 9px;
    font-family: "Arimo", sans-serif; font-weight: 700; font-size: 27px; line-height: 43.5px; color: var(--ink); }
  .specialties__more { position: absolute; left: 0; top: 356px; width: 100%; text-align: center;
    font-family: "Arimo", sans-serif; font-weight: 700; font-size: 27px; color: var(--white); }

  .map { position: absolute; left: 28px; top: 570px; width: 337px; height: 179px; border: 3px solid #333;
    background: linear-gradient(90deg, #f2f2f2 0%, #e4e4e4 70%, #bdbdbd 100%); }
  .locator { position: absolute; left: 360px; top: 565px; width: 170px; height: 200px; }
  .locator__label { position: absolute; right: 8px; top: 1px; font-family: "Archivo Black", sans-serif;
    font-size: 22px; line-height: 26px; color: var(--white); -webkit-text-stroke: 1px var(--ink); text-align: center; }
  .locator__hours { position: absolute; right: 0; top: 64px; text-align: right;
    font-family: "Arimo", sans-serif; font-weight: 700; font-size: 26px; line-height: 33px; color: var(--ink); }
  .locator__time { font-weight: 400; }
  .locator__arrow { position: absolute; left: -80px; top: 0; }

  .back-contact { position: absolute; left: 35px; top: 758px; font-family: "Arimo", sans-serif; color: var(--ink); white-space: nowrap; }
  .back-contact__phone { font-family: "Anton", sans-serif; font-size: 32px; font-weight: 400; letter-spacing: .5px; }
  .back-contact__address { font-size: 16px; }
  .back-location { position: absolute; left: 35px; top: 800px; font-family: "Arimo", sans-serif;
    font-weight: 700; font-size: 16px; color: var(--ink); }
</style>
</head>
<body>
<main class="canvas">

  <section class="side side--front" aria-label="Card front">
    <header class="masthead">
      <span class="masthead__top">Harlow's</span>
      <span class="masthead__main">Crab Shack</span>
    </header>
    <div class="rule"></div>

    <div class="front-body">
      <div class="bubble"></div>
      <div class="seal" role="img" aria-label="Rosette badge with ribbons"></div>
      <p class="seal-text">Family Owned<br>&amp;<br>Operated</p>

      <div class="hours">
        <p class="hours__open">OPEN</p>
        <p class="hours__days">7 DAYS A WEEK:</p>
        <p class="hours__range">MONDAY - SUNDAY:</p>
        <p class="hours__time">11AM - 8PM</p>
      </div>

      <p class="takeaway">TAKEAWAY AVAILABLE</p>
      <p class="kids-menu">KIDS MENU $5.99</p>

      <p class="story">Harlow’s seafood is flown in daily from New England.<br>
        It is our goal to serve the freshest seafood available<br>
        in the Traditional New England style.</p>

      <div class="dish-photo" role="img" aria-label="Photo of a plate of fried fish fillet with fries, salad, lemon and tartar sauce"></div>

      <p class="front-phone">386-517-2293</p>
      <p class="front-address">2738 N Larkspur Rd New Smyrna Beach FL</p>
      <p class="front-web">www.harlowscrabshackqtz.com</p>
    </div>
  </section>

  <section class="side side--back" aria-label="Card back">
    <header class="masthead">
      <span class="masthead__top">Harlow's</span>
      <span class="masthead__main">Crab Shack</span>
    </header>
    <div class="rule"></div>

    <div class="back-body">
      <p class="tagline">Freshest Seafood available<br>in the Traditional<br>New England style</p>

      <div class="specialties">
        <h2 class="specialties__title">SPECIALTIES</h2>
        <ul class="specialties__list">
          <li>Haddock, Cod,</li>
          <li>Mahi, Flounder,</li>
          <li>Fried Oysters,</li>
          <li>Whole Belly Clams,</li>
          <li>NE Steamers,</li>
          <li>Crab Legs, Lobster Salad,</li>
        </ul>
        <p class="specialties__more">and much more!!</p>
      </div>

      <div class="map" role="img" aria-label="Street map of New Smyrna Beach showing the restaurant location on A1A near the ocean"></div>

      <div class="locator">
        <svg class="locator__arrow" width="110" height="80" viewBox="0 0 110 80" aria-hidden="true">
          <path d="M100 20 C70 22 40 30 14 68" fill="none" stroke="#111" stroke-width="2"/>
          <path d="M10 74 L12 58 M10 74 L24 66" fill="none" stroke="#111" stroke-width="2"/>
        </svg>
        <p class="locator__label">WE ARE<br>HERE!!</p>
        <p class="locator__hours">Open<br>7 DAYS<br>a week<br><span class="locator__time">11am-8:00pm</span></p>
      </div>

      <p class="back-contact"><span class="back-contact__phone">386-517-2293</span> <span class="back-contact__address">2738 N Larkspur Rd New Smyrna Beach FL</span></p>
      <p class="back-location">Located on A1A</p>
    </div>
  </section>

</main>
</body>
</html>
```